Business Card Design

Hello!
We would like you to design some business cards for us. We will send you a sample of what we have. We want to take out the Tidewell Harbor Logo and add the RZD logo. This is the company that we own and it manages 7 to 8 franchised child care locations called Pebble Grove. So you can make the Pebble Grove a little logo smaller than what it currently is. Currently the back of the card lists the locations but we don't need that as we are adding new locations every few months. We can also add the website address for RZD below the logo if needed. We don't like the current design so please change it up as you like. Please let us know if you have any questions.

Industry/Entity Type

Business

Contact Information for Business Card

See above

Font styles to use
Serif
Sans Serif

Colors

Designer to choose colors to be used in the design.

Requirements
Must have
• Clean crisp look

```html
<!DOCTYPE html>
<html lang="en">
<head>
<meta charset="utf-8">
<title>Ridgewood Playgroup Management – Business Cards</title>
<link rel="stylesheet" href="https://fonts.googleapis.com/css2?family=Ubuntu:wght@400;500;700&display=swap">
<style>
  :root {
    --brand-red: #d21f2b;
    --band-red: #c81d2a;
    --text-gray: #4a4a4c;
    --card-white: #ffffff;
    --backdrop: #e9e9ea;
  }
  * { margin: 0; padding: 0; box-sizing: border-box; }
  html, body {
    width: 1200px; height: 800px; overflow: hidden;
    background: var(--backdrop);
    font-family: "Ubuntu", Arial, sans-serif;
  }
  .stage { position: relative; width: 1200px; height: 800px; }
  .card {
    position: absolute; width: 520px; height: 297px;
    background: var(--card-white);
    box-shadow: 0 2px 6px rgba(0,0,0,0.12);
    overflow: hidden;
  }
  /* Back of card */
  .card-back { left: 50px; top: 252px; }
  .card-back .frame {
    position: absolute; inset: 20px;
    border: 1.5px solid var(--brand-red);
  }
  .back-brand {
    position: absolute; left: 0; right: 0; top: 96px;
    display: flex; align-items: center; justify-content: center; gap: 12px;
  }
  .brand-square { width: 34px; height: 34px; background: var(--brand-red); flex: none; }
  .brand-name {
    color: var(--brand-red); font-weight: 700; text-transform: uppercase;
    line-height: 1.1; letter-spacing: 0.3px;
  }
  .card-back .brand-name { font-size: 21px; }
  .website {
    position: absolute; left: 0; right: 0; top: 196px; text-align: center;
    color: var(--brand-red); font-size: 13px; font-weight: 500;
  }
  /* Front of card */
  .card-front { left: 630px; top: 252px; }
  .front-brand {
    position: absolute; left: 36px; top: 40px;
    display: flex; align-items: center; gap: 10px;
  }
  .card-front .brand-square { width: 28px; height: 28px; }
  .card-front .brand-name { font-size: 15px; }
  .person { position: absolute; left: 36px; top: 132px; width: 200px; }
  .person-name { color: var(--brand-red); font-size: 17px; font-weight: 700; }
  .person-title { color: var(--text-gray); font-size: 13px; margin-top: 3px; }
  .person-rule { border: 0; border-top: 1.5px solid var(--brand-red); margin-top: 7px; }
  .contact {
    position: absolute; left: 36px; top: 204px;
    color: var(--text-gray); font-size: 12.5px; line-height: 1.55;
  }
  .address-band {
    position: absolute; left: 0; right: 0; bottom: 0; height: 34px;
    background: var(--band-red); color: #fff;
    font-size: 11px; display: flex; align-items: center; padding-left: 36px;
    white-space: nowrap;
  }
</style>
</head>
<body>
<main class="stage">
  <section class="card card-back" aria-label="Back of business card">
    <div class="frame"></div>
    <div class="back-brand">
      <span class="brand-square"></span>
      <span class="brand-name">Ridgewood Playgroup<br>Management</span>
    </div>
    <p class="website">www.pebblegrove.com</p>
  </section>

  <section class="card card-front" aria-label="Front of business card">
    <div class="front-brand">
      <span class="brand-square"></span>
      <span class="brand-name">Ridgewood Playgroup<br>Management</span>
    </div>
    <div class="person">
      <p class="person-name">Noor Amari</p>
      <p class="person-title">Academy Owner</p>
      <hr class="person-rule">
    </div>
    <div class="contact">
      <p>noor.amari@pebblegrove.net</p>
      <p>T. 555.014.2270</p>
    </div>
    <div class="address-band">Management Offices : 418 Linden Crest Road, Unit 4 • Maple Falls, OR 97000</div>
  </section>
</main>
</body>
</html>
```